依頼詳細
現在、お店のロゴはあります。既存のロゴを使用して、立て看板を新しくしたいと思っています。看板の入稿に必要なデザインをillustratorで作成して頂きたいと思います。
重視するポイントは、
1。概要、特徴にも記載しましたが2Fとわかること。
2.ワインはそうですが、お食事ができること。
3.現在使用しているロゴを看板の中心にもっていってワインと一目でわかるようにしたい
4.現在の立て看板がとてもカジュアルな為、店内の雰囲気とかなりギャップがあります。若年の方が立ち飲みバルや、居酒屋、カフェ等と間違えて誤って入ってこられることがたまにあります。お店の雰囲気がでるようなシンプルで雰囲気のあるデザインを希望します。看板製作会社が、完全データの支給を要求しているため、Adobe Illustratorアウトラインデータ Mac=8.0 Win=CSにて納品お願いします。
お店の雰囲気、現在の看板、ロゴなどは添付ファイル参照ください。
記載項目
店舗名、2F、ワインとお食事、今のロゴ。定番メニューのリスト、電話番号。席数。
希望イメージ
シンプル 複雑
単色 カラフル
暗い 明るい
日常 高級
遊び心 厳粛
未来的 伝統的
女性的 男性的
希望する色
白、ワインレッド系、ロゴに合わせたカラー
納品ファイル
• 高解像度JPG (.jpg)
• イラストレーター形式 (.ai)
補足説明
入口の間口が狭いために、看板に必ず2F+↑を記載していただきたいです。表、左上がり、裏、右上がりの☝をつけてほしいです。現在の立て看板ファイルを参照してください。
看板仕上がりサイズはW600×H900です。【画面有効サイズ】 W530×H830mmとなっています。内側に投光機を設置し、ライトアップされます。宜しくお願いいたします。
■ 選んだ理由

現在の問題点をクリアし、お店の雰囲気が看板一つで出ている所。

■ 提案者全員のお礼・コメント

修正等にご対応いただきまして誠にありがとうございました。今後も名刺の修正等依頼していくつもりですので機会がありましたら是非とも宜しくお願いいたします。

```html
<!DOCTYPE html>
<html lang="ja">
<head>
<meta charset="utf-8">
<title>ORVEL WINE &amp; DINE 看板</title>
<link href="https://fonts.googleapis.com/css2?family=Noto+Serif+JP:wght@400;500;700&family=Noto+Sans+JP:wght@500;700&display=swap" rel="stylesheet">
<style>
  :root {
    --wine: #ae2159;
    --wine-light: #c23a70;
    --white: #ffffff;
    --ink: #5b3a2c;
  }
  * { margin: 0; padding: 0; box-sizing: border-box; }
  html, body { width: 800px; height: 1200px; overflow: hidden; background: var(--white); }
  .sign { position: relative; width: 800px; height: 1200px; font-family: "Noto Serif JP", serif; color: var(--white); }

  .upper { position: absolute; left: 0; top: 0; width: 800px; height: 467px; background: var(--wine); }
  .upper::after { content: ""; position: absolute; left: 14px; right: 14px; top: 14px; bottom: 0; border: 2px solid rgba(255,255,255,.45); border-bottom: none; }
  .catch { position: absolute; left: 44px; top: 44px; font-size: 38px; line-height: 60px; font-weight: 500; letter-spacing: 0.02em; }
  .tel { position: absolute; left: 44px; top: 370px; font-size: 38px; font-weight: 400; letter-spacing: 0.02em; }
  .stairs { position: absolute; left: 0; top: 0; }
  .floor { position: absolute; left: 520px; top: 200px; font-family: "Noto Sans JP", sans-serif; font-weight: 700; font-size: 64px; }

  .brand-band { position: absolute; left: 0; top: 467px; width: 800px; height: 333px; background: var(--white); }
  .brand-mark { position: absolute; left: 70px; top: 110px; width: 120px; height: 120px; border-radius: 50%; background: var(--wine); }
  .tagline { position: absolute; left: 282px; top: 52px; color: var(--wine); font-size: 36px; letter-spacing: 0.04em; }
  .brand-name { position: absolute; left: 262px; top: 88px; font-weight: 500; color: var(--ink); font-size: 148px; line-height: 1; letter-spacing: 0.02em; }

  .lower { position: absolute; left: 0; top: 800px; width: 800px; height: 400px; background: var(--wine); }
  .lower::after { content: ""; position: absolute; left: 14px; right: 14px; top: 0; bottom: 14px; border: 2px solid rgba(255,255,255,.45); border-top: none; }
  .menu-head { position: absolute; font-size: 22px; font-weight: 700; line-height: 30px; }
  .menu-list { position: absolute; list-style: none; font-size: 22px; line-height: 30px; white-space: nowrap; }
  .dine-list { font-weight: 700; }
  .note { position: absolute; font-size: 12px; line-height: 14px; opacity: .9; white-space: nowrap; }
  .hours { position: absolute; left: 450px; top: 60px; font-size: 18px; line-height: 26px; white-space: nowrap; }
  .hours dt { float: left; clear: left; width: 130px; }
  .hours dd { margin-left: 130px; }
  .seat { position: absolute; top: 212px; height: 124px; background: var(--white); color: var(--wine); border-radius: 14px; text-align: center; font-family: "Noto Sans JP", sans-serif; font-weight: 700; padding-top: 12px; white-space: nowrap; }
  .seat .label { font-size: 24px; display: block; }
  .seat .count { font-size: 40px; display: block; line-height: 1.3; }
</style>
</head>
<body>
<div class="sign">
  <section class="upper">
    <p class="catch">豊富な種類のワインと<br>築地市場から取り寄せた<br>旬のお食事が楽しめる<br>大人の本格ワインバー</p>
    <svg class="stairs" width="800" height="467" viewBox="0 0 800 467" aria-hidden="true">
      <rect x="575" y="28" width="185" height="420" fill="var(--wine-light)" stroke="#ffffff" stroke-opacity=".6" stroke-width="2"/>
      <circle cx="595" cy="240" r="6" fill="#ffffff" fill-opacity=".7"/>
      <text x="668" y="78" fill="#ffffff" font-family="Noto Serif JP, serif" font-size="20" text-anchor="middle">ORVEL</text>
      <polyline points="400,400 456,400 456,360 510,360 510,318 566,318 566,278 620,278" fill="none" stroke="#ffffff" stroke-width="4"/>
    </svg>
    <div class="floor">2F</div>
    <p class="tel">tel. 090‑4827‑3316</p>
  </section>

  <section class="brand-band">
    <div class="brand-mark"></div>
    <p class="tagline">WINE &amp; DINE</p>
    <h1 class="brand-name">ORVEL</h1>
  </section>

  <section class="lower">
    <h2 class="menu-head" style="left:40px;top:26px;">【WINE】</h2>
    <ul class="menu-list" style="left:52px;top:58px;">
      <li>グラスシャンパーニュ ¥1,300 〜</li>
      <li>グラススパークリング ¥950 〜</li>
      <li>グラスワイン(白・赤) 各種 ¥900 〜</li>
      <li>ボトル各種 ¥4500 〜</li>
    </ul>
    <p class="note" style="left:52px;top:184px;">※その他ビール・グラッパ・ソフトドリンクもご用意しております</p>
    <dl class="hours">
      <dt>営業日</dt><dd>月〜金(土曜 不定休)</dd>
      <dt>定休日</dt><dd>日曜日・祝日</dd>
      <dt>営業時間</dt><dd>18:00-24:00</dd>
      <dt>&nbsp;</dt><dd>(金曜日 25:00まで)</dd>
      <dt>ラストオーダー</dt><dd>23:00</dd>
    </dl>
    <div class="seat" style="left:40px;width:120px;"><span class="label">テーブル</span><span class="count">10席</span></div>
    <div class="seat" style="left:174px;width:136px;"><span class="label">カウンター</span><span class="count">7席</span></div>
    <h2 class="menu-head" style="left:332px;top:208px;">【DINE】</h2>
    <ul class="menu-list dine-list" style="left:360px;top:240px;">
      <li>国産牛トリッパの煮込</li>
      <li>自家製レバーパテ</li>
      <li>季節のお魚のカルパッチョ</li>
      <li>季節の食材を使用したパスタ２種</li>
    </ul>
    <p class="note" style="left:360px;top:364px;">※その他季節に合わせた料理を日替わりでご用意しております</p>
  </section>
</div>
</body>
</html>
```